Web Design with a Twist! Not cheap design

Please note that this project is ending at 5pm on Tuesday the 28th of September, Australian Western Standard Time!!

Please also note that this project has now been guaranteed!

This project involves three primary elements:
* Logo design;
* Web design - of additional pages and page elements to fit into a site that is already in design/development;
* Graphic design - various images used on the site.

The following materials are included for the project:
* Project requirements
* Company / Site name
* Company / Site description
* Wireframes for new pages / page elements
* Screenshots of existing designs and accompanying definition of constraints for new designs
* PSDs for existing site designs
* Technical requirements for designs
* Content (to guide designs)

Project Requirements:

* Logo design:
This is a new company / site, so we need a new logo. We want to see what you come up with here without giving too much direction that may restrict creativity. If desired, you may find possible guidance through considering the company name, company description, and the existing site designs. Please note that the current logo in the site is for placeholder purposes only.

* Web design:
We need the following pages (and features) to be designed for the site:
• Home page
• Advertise page
• How it works page
We’ve provided some wireframes for the pages, however we definitely don't want you to be guided by the layout/styling at all - the wireframes are only there to indicate the features that we require on each page only. So please ignore all aspects of the wireframes except for the indications of features and functionality.

* Graphic design:
We need various images to be designed throughout the site. These include:
• The image at the top of the ‘Home’ page – please note we will provide some direction on this asap
• The image at the top of the ‘Advertise’ page – please note we will provide some direction n this asap
• The image at the top of the ‘How it Works’ pages
• The images that accompany each of the left hand menu items on the ‘How it Works’ pages (the main images & thumbnails if that’s part of your design). Please note that these images need to be constructed to match the Headlines for each of the ‘What’, ‘Who’, ‘Where’, etc menu items. These Headlines (and some descriptive text) can be found in the Content section at the end of this brief.
• The map of Australia for the ‘Home’ page
• The images to accompany the pricing section of the ‘Advertise’ page
• The variations of the ‘Life in the search lane’ images that are used on the ‘Home’, ‘Advertise’, and ‘How it Works’ pages. Please note that if you want to use different imagery (or no imagery, dependent upon your design) for the Home and Advertise pages then this is your call.

Company Name:
TaskBloom

Company / Site description:
This site will provide a means for contractors ('advertisers') to easily specify and advertise their services, coupled with a means for employers (‘buyers’) to easily seek out and contact these people.
The site will cater for contractor-side advertisements only; job postings will not be accommodated (turning the traditional job advertisement model on its head).
In general, the functionality of the site is somewhat like a mashup of sites like crewvault.com and stayvane.com. The site will incorporate the following primary features of contractor profile display and search, company profile display, (and an availability calendar for v2 release).

Constraints for designs:
On some of the existing designs you will notice that a number of the elements of the site have already been designed. When constructing your designs, please work in accordance with the following constraints:

You have to keep:
• Colour scheme in the header
• Colour scheme in the top navigation buttons (including text colour and background colour)
• Colour scheme for the buttons like on the Register page

You can ignore:
• The existing placeholder logo
• Border, layout, and colour scheme for page elements (like the lines around and inside the register section on the Register page)
• Design of text fields
• Font colour scheme throughout the site – the orange and grey headlines and body text
• Design and colour scheme of the map of Australia
• The breadcrumbs (whether or not they appear, and their layout, styling, colour scheme etc)
• Dropdown styling (assuming you had to make some; currently not on any pages we’re asking you to do) like on the Browse Profession page
• Profile styling (for the home page featured profiles) like on the Browse Profession page
• Footer styling
• Anything else we haven’t explicitly asked you to keep

Technical requirements for design:
Any site designs in either Layered Photoshop files (PSD's) or Illustrator Drawings (AI). RGB Color. Must fit current site design, we work to 1024 wide screens. Usuable area is defined in site designs that are attached in the Photoshop documents; it's around 960px.
Logo work needs to be Illustrator Drawings (AI) and EPS. Need CMYK images for printing and RGB for screen. Logos must include any special fonts that are used as TTF or Open Type. Logos need Color, Monochrome, Reversed and both Tall and Wide usages.

Content for the 'How it Works' pages - this content should guide the images that appear on each page.
* What
Headline: TaskBloom brings contractors and employers together
Descriptive text: (turns the traditional job search model on its head)
* Who
Headline: TaskBloom is for highly skilled professionals and fast moving companies
Descriptive text:
* Where
Headline: Anywhere in Australia, TaskBloom is working by your side
Descriptive text:
* Why
Headline: There are more than 1 million reasons to love TaskBloom
Descriptive text: In Australia, there are 1 million people who work as contractors in their main job, and a further 100,000 people who are contractors in their second job. That’s a lot of contractors!
* When
Headline: TaskBloom is forming partnerships 24 hours a day
Descriptive text:
* How
Headline: Life in the search lane, with TaskBloom
Descriptive text: Advertise on TaskBloom now, and get your life in the search lane.

Remember
Just remember the wireframes we have submitted are just a guide – we want to see your creativity shine. And above all else - have fun!
Thank you.
Updates

Please note the deadline for this design competition 5pm on Tuesday the 28th of September, Australian Western Standard Time.

Just under 3 days away!

The deadline of the project will soon be updated to reflect this.

Hi Designers!

Just to be 100% clear about the deadline - the timer is currently showing 7 hours too many. In other words, the project will end 7 hours before the timer finishes.

I will send a notification if the timer starts to display the correct time. So until then, please remember that the deadline is earlier than it seems!

Thanks

Hi Designers,

A couple of really important points:

Firstly - if everyone could please stick to the theme that we provided in the Photoshop files that would be excellent. It is not possible for us to create a new theme. We're dealing with very tight deadlines, so please just provide designs that fit within the current theme.

Secondly, we were really hoping for more illustrations / graphics to be provided in the designs. We're not a fan of the stock photos of generic business people. So please send through designs that incorporate illustrations / graphics for any imagery.

Also just a reminder that this competition is still ending 7 hours earlier than the timer currently displays.

Thanks.

Target Market(s)

The ‘advertiser’ target market for the site is white collar professionals, in all types of industries. The site will be catering for premium contractors only. The site will be catering for both 'in person' contractors, as well as 'knowledge economy' contractors. The site will not be seeking to compete with gigmora.com, plixo.com, taskrune.com, or similar sites.

The advertiser target market will also encompass companies and labour hire agencies that have contractors in their workforce.

The ‘buyer’ target market will encompass employers, recruitment agents, and member-to-member hiring.

Industry/Entity Type

Contractor

Requirements
Must have
• As per overview
Nice to have
• As per overview
Should not have
• As per overview

```html
<!DOCTYPE html>
<html lang="en">
<head>
<meta charset="utf-8">
<title>TaskBloom – Home</title>
<link rel="stylesheet" href="https://fonts.googleapis.com/css2?family=Ubuntu:wght@400;500;700&family=Open+Sans:wght@400;600&display=swap">
<style>
:root{
  --slate:#5e6f86;
  --slate-dark:#4f5f75;
  --tab:#b4bfcb;
  --tab-text:#8595aa;
  --orange:#f26422;
  --orange-deep:#e4510f;
  --peach:#fdd3b7;
  --green:#4fb83a;
  --page:#f7f7f7;
  --text:#2b2b2b;
  --muted:#8d99a8;
  --line:#e2e2e2;
}
*{box-sizing:border-box;margin:0;padding:0}
html,body{width:940px;height:1200px;overflow:hidden}
body{background:var(--page);font-family:"Open Sans",Verdana,sans-serif;color:var(--text);position:relative}
.abs{position:absolute}

.site-header{left:0;top:0;width:940px;height:113px;background:linear-gradient(#66768c,var(--slate))}
.brand{left:28px;top:14px;width:230px;height:91px;background:linear-gradient(var(--orange),var(--orange-deep));box-shadow:0 2px 4px rgba(0,0,0,.3);display:flex;align-items:center;justify-content:center;font-family:"Ubuntu",sans-serif;font-weight:500;font-size:34px;color:#fff;letter-spacing:1px}
.nav-tab{top:83px;height:30px;background:var(--tab);border-radius:6px 6px 0 0;font-family:"Ubuntu",sans-serif;font-weight:500;font-size:16px;color:var(--tab-text);display:flex;align-items:center;justify-content:center}
.nav-tab.is-home{background:var(--page)}

.search{left:679px;top:126px;width:232px;height:24px;border:1px solid #a9b4c2;border-radius:3px;background:#fff;display:flex;overflow:hidden}
.search-field{flex:1;display:flex;align-items:center;gap:5px;padding-left:7px;font-size:12px;color:#8a96a5}
.search-go{width:38px;background:var(--slate);color:#fff;font-weight:600;font-size:12px;display:flex;align-items:center;justify-content:center}

.hero{left:28px;top:160px;width:883px;height:246px;background:#fff;border:1px solid var(--line)}
.hero-title{left:30px;top:34px;font-family:"Ubuntu",sans-serif;font-size:18px}
.hero-title b,.welcome-title b{color:var(--orange);font-weight:500}
.hero-title b{font-size:22px}
.hero-copy{left:29px;top:71px;width:370px;font-size:11.6px;line-height:17px}
.btn-read{left:29px;top:198px;width:107px;height:26px;background:var(--orange);border-radius:3px;color:#fff;font-family:"Ubuntu",sans-serif;font-weight:500;font-size:15px;display:flex;align-items:center;justify-content:center}
.dots{left:297px;top:206px;display:flex;gap:10px}
.dots span{width:9px;height:9px;border-radius:50%;background:#c9c9c9}
.dots span.on{background:var(--orange)}
.hero-photo{left:422px;top:10px;width:447px;height:222px;background:linear-gradient(135deg,#f1f3f6,#cdd5df 60%,#aebbc9);border:3px solid #fff;box-shadow:0 0 4px rgba(0,0,0,.35)}

.welcome-title{left:29px;top:418px;font-family:"Ubuntu",sans-serif;font-size:24px}
.welcome-copy{left:29px;top:451px;width:572px;font-size:11.6px;line-height:17px}
.welcome-copy p{margin-bottom:17px}

.ad-banner{left:30px;top:701px;width:399px;height:128px;border-radius:7px;background:linear-gradient(#6c7c93,#56667d);box-shadow:0 2px 5px rgba(0,0,0,.45);color:#fff;text-align:center;font-family:"Ubuntu",sans-serif}
.ad-banner h2{font-weight:400;font-size:44px;margin-top:12px;letter-spacing:1px}
.ad-banner p{font-size:28px;margin-top:6px}

.finder{left:622px;top:432px;width:289px;height:397px;background:var(--peach);border:1px solid var(--orange);border-radius:8px}
.finder-box{left:36px;top:18px;width:236px;height:248px;background:var(--orange)}
.finder-box h3{font-family:"Ubuntu",sans-serif;font-weight:500;font-size:17px;color:#fff;text-align:center;margin-top:16px;line-height:20px}
.finder-map{left:36px;top:76px;width:166px;height:152px;background:linear-gradient(#fde4d6,#f9c9ae);border-radius:40% 50% 45% 40%}
.finder-badge{left:6px;top:35px;width:32px;height:32px;background:var(--orange);border-radius:4px 0 0 4px;display:flex;align-items:center;justify-content:center}
.finder-input{left:36px;top:286px;width:235px;height:34px;background:#fff;border:1px solid #d6d6d6;border-radius:3px;font-size:12px;letter-spacing:.5px;display:flex;align-items:center;justify-content:center}
.finder-btn{left:36px;top:334px;width:235px;height:35px;background:var(--green);border-radius:3px;color:#fff;font-family:"Ubuntu",sans-serif;font-weight:500;font-size:17px;display:flex;align-items:center;justify-content:center}

.featured-title{left:28px;top:878px;font-family:"Ubuntu",sans-serif;font-size:24px;color:var(--orange)}
.featured{left:28px;top:914px;width:883px;height:133px;background:#fff;border:1px solid var(--line)}
.profile{top:12px;width:270px;height:107px;border:1px solid var(--orange);background:linear-gradient(#fff,#f1f1f1)}
.profile-mark{left:10px;top:20px;width:92px;height:64px;display:flex;align-items:center;justify-content:center;gap:5px;font-family:"Ubuntu",sans-serif;font-size:18px;color:#2f3c55}
.profile-mark i{width:12px;height:12px;border-radius:50%;background:#c9a43a}
.profile h4{left:104px;top:8px;font-family:"Ubuntu",sans-serif;font-weight:400;font-size:18px}
.profile p{left:104px;top:34px;width:160px;font-size:12.4px;line-height:14px}
.profile a{left:104px;top:91px;font-family:"Ubuntu",sans-serif;font-weight:500;font-size:11px;letter-spacing:.5px;color:var(--text);text-decoration:none}

.site-footer{left:30px;top:1106px;width:868px;border-top:1px solid var(--line);font-family:Arial,sans-serif;font-size:11px}
.foot-col{top:12px;line-height:15px;color:#b8c0ca}
.foot-col strong{display:block;color:var(--slate);font-size:11.5px;margin-bottom:5px}
.copyright{right:0;top:12px;color:var(--slate)}
</style>
</head>
<body>

<header class="site-header abs">
  <div class="brand abs">TaskBloom</div>
  <nav>
    <div class="nav-tab is-home abs" style="left:287px;width:54px">
      <svg width="18" height="17" viewBox="0 0 18 17"><path d="M9 1 1 8h2.5v8h4v-5h3v5h4V8H17z" fill="#7f8ea3"/></svg>
    </div>
    <div class="nav-tab abs" style="left:350px;width:66px">FIND</div>
    <div class="nav-tab abs" style="left:426px;width:111px">ADVERTISE</div>
    <div class="nav-tab abs" style="left:546px;width:143px">HOW IT WORKS</div>
    <div class="nav-tab abs" style="left:699px;width:81px">BLOG</div>
    <div class="nav-tab abs" style="left:790px;width:81px">LOGIN</div>
  </nav>
</header>

<form class="search abs">
  <div class="search-field">
    <svg width="14" height="14" viewBox="0 0 14 14"><circle cx="5.5" cy="5.5" r="4.2" fill="none" stroke="#9aa6b5" stroke-width="1.8"/><path d="M8.6 8.6 13 13" stroke="#9aa6b5" stroke-width="2"/></svg>
    Find a contractor
  </div>
  <div class="search-go">Go</div>
</form>

<section class="hero abs">
  <h1 class="hero-title abs">Changing how you <b>Find Job</b></h1>
  <p class="hero-copy abs">Lorem Ipsum is simply dummy text of the printing and typesetting industry. Lorem Ipsum has been the industry's standard dummy text ever since the 1500s, when an unknown printer took a galley of type and scrambled it to make a type specimen book. It has survived not only five centuries, but also the leap into electronic typesetting, remaining essentially unchanged.</p>
  <div class="btn-read abs">Read More</div>
  <div class="dots abs"><span class="on"></span><span></span><span></span></div>
  <div class="hero-photo abs" role="img" aria-label="Photo of two professionals reviewing a document at a laptop"></div>
</section>

<h2 class="welcome-title abs">Welcome to <b>TaskBloom</b></h2>
<div class="welcome-copy abs">
  <p>Lorem Ipsum is simply dummy text of the printing and typesetting industry. Lorem Ipsum has been the industry's standard dummy text ever since the 1500s, when an unknown printer took a galley of type and scrambled it to make a type specimen book. It has survived not only five centuries, but also the leap into electronic typesetting, remaining essentially unchanged.</p>
  <p>Lorem Ipsum is simply dummy text of the printing and typesetting industry. Lorem Ipsum has been the industry's standard dummy text ever since the 1500s, when an unknown printer took a galley of type and scrambled it to make a type specimen book. It has survived not only five centuries, but also the leap into electronic typesetting, remaining essentially unchanged.</p>
  <p>Lorem Ipsum is simply dummy text of the printing and typesetting industry. Lorem Ipsum has been the industry's standard dummy text ever since the 1500s, when an unknown printer took a galley of type and scrambled it to make a type specimen book.</p>
</div>

<div class="ad-banner abs">
  <h2>ADVERTISE</h2>
  <p>Life In The Search Lane</p>
</div>

<aside class="finder abs">
  <div class="finder-box abs">
    <h3>Find Highly Skilled<br>Professionals:</h3>
    <div class="finder-map abs" role="img" aria-label="Map of Australia divided into states"></div>
  </div>
  <div class="finder-badge abs">
    <svg width="18" height="18" viewBox="0 0 18 18" fill="none" stroke="#fff" stroke-width="1.4"><circle cx="9" cy="9" r="7.5"/><ellipse cx="9" cy="9" rx="3.3" ry="7.5"/><path d="M1.5 9h15M3 5h12M3 13h12"/></svg>
  </div>
  <div class="finder-input abs">Keyword...</div>
  <div class="finder-btn abs">FIND CONTRACTORS</div>
</aside>

<h2 class="featured-title abs">Featured Profiles:</h2>
<section class="featured abs">
  <article class="profile abs" style="left:10px">
    <div class="profile-mark abs"><i style="background:#7fb82e"></i></div>
    <h4 class="abs">Company Name:</h4>
    <p class="abs">Lorem Ipsum is simply dummy text of the printing and typesetting industry.</p>
    <a class="abs">Read More</a>
  </article>
  <article class="profile abs" style="left:308px">
    <div class="profile-mark abs">Arvolo</div>
    <h4 class="abs">Company Name:</h4>
    <p class="abs">Lorem Ipsum is simply dummy text of the printing and typesetting industry.</p>
    <a class="abs">Read More</a>
  </article>
  <article class="profile abs" style="left:602px">
    <div class="profile-mark abs"><i></i>Nexqa</div>
    <h4 class="abs">Company Name:</h4>
    <p class="abs">Lorem Ipsum is simply dummy text of the printing and typesetting industry.</p>
    <a class="abs">Read More</a>
  </article>
</section>

<footer class="site-footer abs">
  <div class="foot-col abs" style="left:1px"><strong>About Us</strong>Features<br>Pricing<br>Team</div>
  <div class="foot-col abs" style="left:76px"><strong>Browse</strong>By State<br>By Business<br>Search</div>
  <div class="foot-col abs" style="left:156px"><strong>Sign up</strong></div>
  <div class="copyright abs">© Copyright 2010 TaskBloom</div>
</footer>

</body>
</html>
```